Kids School Holiday Tennis Camp Flyer

We are a small tennis center based in Sydney's Eastern Suburbs - Australia.
We run coaching programs for kids and adults and also during school holidays organise fun tennis camps for kids aged 6-15 yrs.
Our website is www.brightvolleycourts.com but we dont necessarily need the flyer to tie in with the website design, although happy to have any advice on this.
We would like our logo on there and lots of bright kids colours .... especially yellow's (like tennis balls) and greens (like grass courts).
We would like to convey the message of fun, games, sunshine, interaction but also fitness and learning new tennis skills ..... so its not a play school but a true tennis camp. However - it is also fun to attend and meet other kids.
We would like a double sided flyer if possible with the next terms coaching advertised on the back.
Tennis camp dates to be listed :
Spring Tennis Camps WEEK 1 : Mon Sept 24th - Fri Sept 28th
WEEK 2: Tues Oct 2nd - Fri Oct 5th
Summer Tennis Camps WEEK 1 : Mon Jan 7th - Fri Jan 11th
WEEK 2: Mon Jan 14th - Fri Jan 18th
WEEK 3: Mon Jan 21st - Fri Jan 25th
Flip side of the flyer to advertise kids school term coaching:
Term 4 kids tennis is an 11 week terms, starts Monday October 8th and runs until Friday Dec 21st
Term 1 2013 is also an 11 week term running from Mon Jan 28th to Fri April 12th.
Target Market(s)
Its a kids tennis camp but the parents will be the buyer - so it must have a kids feel but also appeal to the mum and dads !
Industry/Entity Type
Fitness
Look and feel

```html
<!DOCTYPE html>
<html lang="en">
<head>
<meta charset="utf-8">
<title>Kids School Holiday Tennis Camp Flyer</title>
<link href="https://fonts.googleapis.com/css2?family=Fredoka:wght@500;600&display=swap" rel="stylesheet">
<style>
  :root {
    --stage: #e6e6e4;
    --paper: #fdf4ea;
    --grass: #45b54a;
    --ball: #e2e43c;
    --ink: #222222;
    --racket-red: #e8323f;
    --racket-blue: #3f63b0;
    --frame-warm: #f6b36a;
    --frame-sun: #eeee86;
    --frame-leaf: #8fd08f;
    --frame-sky: #8fd6ef;
  }
  * { margin: 0; padding: 0; box-sizing: border-box; }
  html, body { width: 1200px; height: 900px; overflow: hidden; }
  body {
    background: var(--stage);
    font-family: "Fredoka", "Arial Rounded MT Bold", sans-serif;
    position: relative;
  }
  .side-label {
    position: absolute; top: 61px; width: 500px; text-align: center;
    font-family: Arial, Helvetica, sans-serif; font-size: 18px; color: var(--ink);
  }
  .side-label.front { left: 73px; }
  .side-label.back { left: 626px; }

  .flyer-page {
    position: absolute; top: 97px; width: 500px; height: 706px;
    background: var(--paper); color: var(--grass); font-weight: 600;
  }
  .flyer-page.front { left: 73px; }
  .flyer-page.back { left: 626px; }

  .border-band {
    position: absolute; left: 26px; top: 26px; width: 450px; height: 652px;
    border: 18px solid transparent; border-radius: 9px;
    background:
      linear-gradient(var(--paper), var(--paper)) padding-box,
      linear-gradient(135deg, var(--frame-leaf), var(--frame-sun) 30%, var(--frame-warm) 55%, var(--frame-sky) 80%, var(--frame-leaf)) border-box;
  }

  .racket-art {
    position: absolute; left: 78px; top: 72px; width: 276px; height: 278px; border-radius: 24px;
    background: linear-gradient(135deg, var(--racket-red) 0%, #f1a3a8 48%, #a8b8e0 52%, var(--racket-blue) 100%);
    opacity: 0.85;
  }
  .camp-title {
    position: absolute; left: 0; right: 0; top: 372px; text-align: center;
    font-size: 42px; line-height: 41px; letter-spacing: 0.5px; font-weight: 600;
  }
  .term-info {
    position: absolute; left: 40px; right: 40px; top: 516px; text-align: center;
    font-size: 17.5px; line-height: 19.5px; white-space: nowrap;
  }

  .season-heading {
    position: absolute; left: 75px; font-size: 32px; line-height: 36px; font-weight: 600; white-space: nowrap;
  }
  .season-rule { position: absolute; left: 75px; height: 8px; background: var(--grass); }
  .week-label, .week-dates {
    position: absolute; left: 75px; font-size: 25px; line-height: 28px; white-space: nowrap;
  }
  .week-num {
    display: inline-block; width: 26px; height: 26px; border-radius: 50%;
    background: var(--ball); text-align: center; line-height: 26px; margin-left: 2px;
  }
  .more-info {
    position: absolute; left: 75px; top: 613px; font-size: 12px; line-height: 14px;
  }
  .brand-mark {
    position: absolute; left: 355px; top: 574px; width: 76px; height: 64px;
    display: flex; align-items: center; justify-content: center; gap: 4px;
  }
  .brand-dot { width: 10px; height: 10px; border-radius: 50%; background: var(--ball); flex: none; }
  .brand-name { font-size: 13px; line-height: 15px; color: var(--grass); font-weight: 600; }
</style>
</head>
<body>
  <div class="side-label front">Front</div>
  <div class="side-label back">Back</div>

  <section class="flyer-page front">
    <div class="border-band" role="img" aria-label="Decorative border of colourful tennis balls around the page"></div>

    <div class="racket-art" role="img" aria-label="Illustration of a red and a blue tennis racket crossed over a yellow tennis ball"></div>

    <h1 class="camp-title">KIDS SCHOOL<br>HOLIDAY<br>TENNIS CAMP</h1>

    <p class="term-info">Term 4 kids tennis is an 11 week<br>terms, starts Monday October 8th<br>and runs until Friday Dec 21st.<br>Term 1 2013 is also an 11 week<br>term running from Mon Jan 28th<br>to Fri April 12th.</p>
  </section>

  <section class="flyer-page back">
    <div class="border-band" role="img" aria-label="Decorative border of colourful tennis balls around the page"></div>

    <h2 class="season-heading" style="top:74px">Spring Tennis Camps</h2>
    <div class="season-rule" style="top:113px; width:302px"></div>
    <div class="week-label" style="top:141px">Week <span class="week-num">1</span></div>
    <div class="week-dates" style="top:168px">Mon Sept 24th – Fri Sept 28th</div>
    <div class="week-label" style="top:211px">Week <span class="week-num">2</span></div>
    <div class="week-dates" style="top:238px">Tues Oct 2nd – Fri Oct 5th</div>

    <h2 class="season-heading" style="top:297px">Summer Tennis Camps</h2>
    <div class="season-rule" style="top:335px; width:323px"></div>
    <div class="week-label" style="top:366px">Week <span class="week-num">1</span></div>
    <div class="week-dates" style="top:393px">Mon Jan 7th – Fri Jan 11th</div>
    <div class="week-label" style="top:434px">Week <span class="week-num">2</span></div>
    <div class="week-dates" style="top:461px">Mon Jan 14th – Fri Jan 18th</div>
    <div class="week-label" style="top:500px">Week <span class="week-num">3</span></div>
    <div class="week-dates" style="top:527px">Mon Jan 21st – Fri Jan 25th</div>

    <p class="more-info">For more information please<br>goto www.brightvolleycourts.com</p>

    <div class="brand-mark">
      <span class="brand-dot"></span>
      <span class="brand-name">Bright<br>Volley</span>
    </div>
  </section>
</body>
</html>
```